Packaging Design for Vorimelt a Company Providing a Convenient and Complete Alternative to Food

We need a packaging and label design for Vorimelt. Vorimelt stands for nutrient balance and it is a meal alternative that comes in a powder that has all the nutrients needed for a complete and balanced meal. Vorimelt would be used by people that are hungry but don't have time to cook, are in a rush, or simply want to get the healthiest meal they can as conveniently as possible. We were thinking of using a modern and simple design that would attract consumers in the 22-28 age bracket. I want the packaging to be cool and attractive using blue and orange/red (an orangey red) since those are the colors of the logo

Now that being said, Vorimelt is more about a lifestyle than the product itself. The website still doesn't reflect this because the first step for me in creating it was to put in all the hard info and facts and then slowly transform it to what I want it to be. Vorimelt's "slogan" is spark every hour and the idea is that the product will be used by people who are busy having too much fun in life so they don't have time to cook so they choose to have Vorimelt. For example a commercial we are producing starts with first person footage of me getting in a skyvane 40 and then doing all sorts of water sports and having fun in the beach. At the end, there's a hot girl in a boat making a vorimelt and drinking it. So as you can see it's not about the product itself but what we want people to feel when they think about it and part of what they feel will be conveyed by the logo.

I want to convey a sense of energy and fun. I want people to feel inspired and feel something when they see the packaging since this is the same logo that will go on the product packaging (I will hold another project for that as soon as this one ends).

Our target market is a young professional probably with higher disposable income than your average 24-35 year old, trendy, modern, sophisticated and often consumes premium brands and therefore the packaging must reflect that.

The bottle will use a shrink sleeve that will wrap around from the bottom of the bottle up to the neck. The bottle is white, with a white smooth cap. I want the design to be able to blend in with the white of the bottle so that it all flows. I was thinking of maybe leaving some parts transparent so that the white of the bottle shows instead of using white but I honestly don't know if that would be a good idea.

Attached you will find the template for the shrink sleeve, the logo and the tub. The picture of the bottle is only a reference so that you can know what size it will be.

I'm going to need the design both in the template and on the tub. Make it look nice since I might be using the designs as a background in the website and definitely as the product image (what people will be clicking on to buy it)

Here are the things that need to be on the tub (these will be modified later only to be used as a placeholder for now):

Under the logo or in the front and middle of the tub (under Vorimelt probably):
A Complete and Balanced Meal Alternative.

It needs to say its vanilla flavored

It needs to have the supplement facts (just put any random numbers)

Directions: Use 2-4 scoops depending on your level of hunger. Mix 5 ounces of water per scoop in a thermos, shaker cup, or closed bottle and shake vigorously for ten seconds. Drink and enjoy!

What is Vorimelt?
Vorimelt is a complete and balanced meal alternative that gives your body all the right nutrients to keep it functioning at its full potential. Vorimelt will nourish your body with good proteins, carbohydrates, fats, and micro-nutrients (like vitamins and minerals) so that you don't have to worry about cooking or eating the right stuff. We take care of everything for you so that you can keep on doing what you love, whatever that may be. Vorimelt will spark every hour!
For more information go to Vorimelt.example

Hey i forgot to add that its gonna be vanilla flavored

```html
<!DOCTYPE html>
<html lang="en">
<head>
<meta charset="utf-8">
<title>Vorimelt DashMeal – Vanilla Label</title>
<link rel="stylesheet" href="https://fonts.googleapis.com/css2?family=Oswald:wght@500;600&family=Poppins:wght@500;600&family=Roboto+Slab:wght@300&display=swap">
<style>
  :root {
    --backdrop: #eceef1;
    --label-white: #ffffff;
    --brand-red: #e53c2e;
    --brand-orange: #f07a2a;
    --brand-amber: #f2a33a;
    --brand-blue: #1f6fb5;
    --fresh-green: #7cc242;
    --ink-white: #ffffff;
  }
  * { box-sizing: border-box; margin: 0; padding: 0; }
  html, body {
    width: 1200px; height: 1128px; overflow: hidden;
    background: var(--backdrop);
  }
  .label {
    position: absolute; left: 111px; top: 56px;
    width: 515px; height: 535px;
    transform: scale(1.9); transform-origin: top left;
    background: var(--label-white);
    overflow: hidden;
    box-shadow: 0 2px 6px rgba(0,0,0,.12);
  }
  .top-strip {
    position: absolute; left: 0; top: 0; width: 100%; height: 20px;
    background: var(--brand-red);
  }
  .web-address {
    position: absolute; left: 12px; top: 2px;
    font: 600 12px/16px "Poppins", sans-serif; color: var(--ink-white);
  }
  .brand-header {
    position: absolute; left: 208px; top: 0; width: 307px; height: 68px;
    background: linear-gradient(90deg, var(--brand-red), var(--brand-orange) 60%, var(--brand-amber));
    border-bottom-left-radius: 22px;
  }
  .brand-lockup {
    position: absolute; left: 12px; top: 18px;
    display: flex; align-items: center; gap: 8px;
  }
  .brand-dot {
    width: 30px; height: 30px; border-radius: 50%;
    background: var(--label-white);
  }
  .brand-name {
    font: 500 19px/1 "Poppins", sans-serif; color: var(--brand-blue);
    letter-spacing: .5px;
  }
  .brand-slogan {
    position: absolute; right: 14px; top: 44px;
    font: 500 12px/1 "Poppins", sans-serif; color: var(--ink-white);
  }
  .tagline-strip {
    position: absolute; left: 45px; top: 35px; width: 20px; height: 462px;
    background: var(--fresh-green);
  }
  .tagline {
    position: absolute; left: 45px; top: 497px;
    width: 462px; height: 20px;
    transform: rotate(-90deg); transform-origin: top left;
    font: 600 14.5px/20px "Poppins", sans-serif; color: var(--ink-white);
    text-align: center; letter-spacing: .3px;
  }
  .product-name {
    position: absolute; left: 80px; top: 512px;
    width: 480px; height: 110px;
    transform: rotate(-90deg); transform-origin: top left;
    font: 300 104px/110px "Roboto Slab", serif; color: var(--brand-red);
    white-space: nowrap;
  }
  .macros { position: absolute; left: 220px; top: 103px; list-style: none; }
  .macro { display: flex; align-items: center; height: 44px; margin-bottom: 18px; }
  .macro-badge {
    width: 44px; height: 44px; border-radius: 50%;
    background: var(--brand-red); border: 4px solid var(--fresh-green);
    display: flex; align-items: center; justify-content: center;
    font: 500 17px/1 "Oswald", sans-serif; color: var(--ink-white);
  }
  .macro-name {
    margin-left: 12px;
    font: 600 26px/1 "Oswald", sans-serif; color: var(--brand-red);
    letter-spacing: 1px;
  }
  .format-band {
    position: absolute; left: 218px; top: 278px; width: 297px; height: 92px;
    background: var(--brand-red);
    font: 500 40px/1 "Oswald", sans-serif; color: var(--ink-white);
    padding: 24px 0 0 18px;
  }
  .flavor-band {
    position: absolute; left: 218px; top: 368px; width: 297px; height: 44px;
    background: var(--brand-amber);
    font: 500 28px/44px "Oswald", sans-serif; color: var(--brand-red);
    padding-left: 78px;
  }
  .product-story {
    position: absolute; left: 218px; top: 430px; width: 292px;
    font: 500 8.6px/11px "Oswald", sans-serif; color: var(--brand-red);
  }
  .base-strip {
    position: absolute; left: 0; bottom: 0; width: 100%; height: 10px;
    background: var(--brand-red);
  }
</style>
</head>
<body>
  <main class="label">
    <div class="top-strip"><span class="web-address">www.vorimelt.example</span></div>

    <header class="brand-header">
      <div class="brand-lockup">
        <span class="brand-dot"></span>
        <span class="brand-name">VORIMELT</span>
      </div>
      <span class="brand-slogan">Spark Every Hour!</span>
    </header>

    <div class="tagline-strip"></div>
    <p class="tagline">TAKE YOUR FOOD TO THE NEXT LEVEL</p>

    <h1 class="product-name">DashMeal</h1>

    <ul class="macros">
      <li class="macro"><span class="macro-badge">40%</span><span class="macro-name">CARBS</span></li>
      <li class="macro"><span class="macro-badge">30%</span><span class="macro-name">PROTEIN</span></li>
      <li class="macro"><span class="macro-badge">30%</span><span class="macro-name">FAT</span></li>
    </ul>

    <div class="format-band">POWDERED FOOD</div>
    <div class="flavor-band">VANILLA FLAVOR</div>

    <p class="product-story">Although a great option for anytime, DashMeal especially shines when you just don't have enough time to prepare a healthy meal and want a nutritious alternative. DashMeal, the most balanced food on Earth, contains a ratio of 40% carbs, 30% protein and 30% fat – a ratio ideal for optimal health and hormonal balance. The most amazing part about DashMeal is the extracts of fruits and vegetables that deliver the broad spectrum of micronutrients, phytonutrients and carotenoids that the body craves and needs.</p>

    <div class="base-strip"></div>
  </main>
</body>
</html>
```